Label Design for Food Brand

We want a modern label for our spice blends. We are completely open in which direction, it should be modern and beautiful.

Use for Sample spice mixture: "BBQ Tanqo"

Here the Packaging:
https://www.orv-plimkevar.com/media/xlarge/1700_1.jpg
Abmessung: Ø 54 x 67 mm

Target Market(s)

Food

Industry/Entity Type

Food

Requirements
Must have
• Logo, Name of Tanqo
Should not have
• Images of food

```html
<!DOCTYPE html>
<html lang="en">
<head>
<meta charset="utf-8">
<title>BBQ Tanqo – Spice Label</title>
<link rel="stylesheet" href="https://fonts.googleapis.com/css2?family=Montserrat:wght@300;400;700;800&display=swap">
<style>
  :root {
    --page: #ffffff;
    --label-dark: #1c1c1c;
    --label-mid: #3a3a3a;
    --ink-light: #ffffff;
    --ink-dark: #151515;
    --band: #f2f2f2;
    --rule: #e6e6e6;
  }
  * { margin: 0; padding: 0; box-sizing: border-box; }
  html, body {
    width: 1200px;
    height: 750px;
    overflow: hidden;
    background: var(--page);
    font-family: "Montserrat", sans-serif;
  }
  .label {
    position: absolute;
    left: 110px;
    top: 75px;
    width: 980px;
    height: 600px;
    background: radial-gradient(ellipse at 60% 45%, var(--label-mid) 0%, var(--label-dark) 70%);
    color: var(--ink-light);
    overflow: hidden;
  }
  .brand-band {
    position: absolute;
    left: 40px;
    top: 90px;
    width: 120px;
    height: 430px;
    background: var(--band);
    display: flex;
    align-items: center;
    justify-content: center;
  }
  .brand-name {
    transform: rotate(-90deg);
    white-space: nowrap;
    font-size: 52px;
    font-weight: 700;
    letter-spacing: 1px;
    color: var(--ink-dark);
  }
  .product {
    position: absolute;
    left: 215px;
    top: 60px;
  }
  .product-type {
    display: block;
    font-size: 210px;
    font-weight: 300;
    line-height: 0.9;
    letter-spacing: -4px;
  }
  .product-name {
    display: block;
    font-size: 150px;
    font-weight: 800;
    line-height: 0.95;
    letter-spacing: -2px;
  }
  .tagline {
    position: absolute;
    left: 220px;
    top: 395px;
    font-size: 31px;
    line-height: 1.1;
    font-weight: 400;
    letter-spacing: 0.5px;
  }
  .tagline strong { font-weight: 800; }
  .claims {
    position: absolute;
    left: 220px;
    top: 478px;
    width: 700px;
    height: 80px;
    border-top: 3px solid var(--rule);
  }
  .claim {
    position: absolute;
    top: 0;
    font-size: 22px;
    letter-spacing: 0.5px;
    font-weight: 400;
  }
  .claim strong { font-weight: 800; }
  .claim--gluten { left: 20px; top: 40px; }
  .claim--msg { left: 330px; top: 16px; }
  .claim--soy { left: 560px; top: 16px; }
  .claims svg { position: absolute; left: 0; top: 0; }
</style>
</head>
<body>
  <section class="label">
    <div class="brand-band">
      <span class="brand-name">TANQOFOOD</span>
    </div>

    <h1 class="product">
      <span class="product-type">BBQ</span>
      <span class="product-name">TANQO</span>
    </h1>

    <p class="tagline">HANDCRAFTED WITH <strong>HIGHEST</strong><br><strong>QUALITY INGREDIENTS</strong></p>

    <div class="claims">
      <svg width="700" height="80" viewBox="0 0 700 80" aria-hidden="true">
        <line x1="0" y1="28" x2="290" y2="28" stroke="#e6e6e6" stroke-width="3"/>
        <line x1="290" y1="0" x2="290" y2="78" stroke="#e6e6e6" stroke-width="4"/>
        <line x1="520" y1="0" x2="520" y2="60" stroke="#e6e6e6" stroke-width="4"/>
      </svg>
      <span class="claim claim--gluten">GLUTEN <strong>FREE</strong></span>
      <span class="claim claim--msg">NO <strong>MSG</strong></span>
      <span class="claim claim--soy">NO <strong>SOY</strong></span>
    </div>
  </section>
</body>
</html>
```